Springtime Saver Special Promotional Postcard

I would like a postcard designed for a credit card balance transfer promotion.

The title for this promotion is "Springtime saver special".

(This paragraph should not be used word for word) Credit Card rates are on the rise since the Federal Prime Rate increase. I want to promote a non-variable rate credit card with rates as low as 7.9% APR* and free balance transfers. Simple, straightforward card with a low rate. There is no intro APR, always a great rate.

Below is some sample content options to highlight:
$0 Annual Fee
$0 Balance Transfer Fee
No Teaser, No Intro, just a great rate

Not only could you cut your interest rate in half, but you will also save hundreds of dollars by not paying any balance transfer fees.

Apply Today! www.brivantalend.org

Target Market(s)

Ages 25-45

Industry/Entity Type

Credit Card

Requirements
Must have
• Required disclaimer: *Annual Percentage Rate. 7.9% is the preferred rate based on qualifying credit. (teeny tiny disclaimer on front of card where rate is being advertised)
• Tagline: When you need OPTIONS ... (should be placed on back of postcard by credit union name, address, and logo)

```html
<!DOCTYPE html>
<html lang="en">
<head>
<meta charset="utf-8">
<title>Springtime Saver Special Postcard</title>
<link rel="stylesheet" href="https://fonts.googleapis.com/css2?family=Lobster+Two:ital,wght@1,700&family=Open+Sans:wght@400;600;700&display=swap">
<style>
  :root {
    --red: #d8192e;
    --red-deep: #b3111f;
    --red-text: #9b1b2a;
    --panel-grey: #e6e7e9;
    --ink: #4a4a4a;
    --ink-soft: #6d6e71;
    --charcoal: #3b3b3c;
    --paper: #ffffff;
    --backdrop: #ebe8e4;
    --rule: #c9c9c9;
  }
  * { box-sizing: border-box; margin: 0; padding: 0; }
  html, body { width: 865px; height: 1200px; overflow: hidden; }
  body {
    background: var(--backdrop);
    font-family: "Open Sans", Arial, sans-serif;
    position: relative;
  }
  .postcard {
    position: absolute;
    width: 642px;
    height: 496px;
    background: var(--paper);
    overflow: hidden;
    box-shadow: 0 3px 10px rgba(0,0,0,.18);
  }
  .postcard--front { left: 71px; top: 71px; }
  .postcard--back { left: 155px; top: 632px; }
  .postcard svg.shapes { position: absolute; inset: 0; }

  /* Front */
  .front-header {
    position: absolute; left: 0; top: 0; width: 642px; height: 109px;
    background: linear-gradient(180deg, var(--red) 0%, var(--red-deep) 100%);
  }
  .brand-name {
    position: absolute;
    font-family: "Open Sans", Arial, sans-serif;
    font-weight: 600;
    line-height: 1.1;
  }
  .front-header .brand-name { left: 28px; top: 34px; color: #fff; font-size: 17px; }
  .promo-title {
    position: absolute;
    font-family: "Lobster Two", cursive;
    font-style: italic;
    font-weight: 700;
    white-space: nowrap;
  }
  .front-header .promo-title { right: 28px; top: 22px; color: #fff; font-size: 38px; }
  .intro {
    position: absolute; left: 334px; top: 139px;
    color: var(--ink-soft); font-size: 14.5px; line-height: 1.35;
  }
  .benefits {
    position: absolute; left: 300px; top: 196px; width: 342px; height: 152px;
    background: var(--panel-grey);
    list-style: none;
    padding: 10px 0 0 50px;
  }
  .benefits li {
    position: relative;
    color: var(--red-text); font-weight: 700; font-size: 14px; line-height: 1.2;
    padding-left: 18px; margin-bottom: 11px;
  }
  .benefits li svg { position: absolute; left: 0; top: 4px; }
  .savings {
    position: absolute; left: 363px; top: 364px; width: 265px;
    color: var(--ink); font-size: 10.5px; line-height: 1.4;
  }
  .disclaimer {
    position: absolute; left: 382px; top: 436px;
    color: var(--ink-soft); font-size: 7px; white-space: nowrap;
  }
  .front-footer {
    position: absolute; left: 0; top: 455px; width: 642px; height: 41px;
    background: linear-gradient(180deg, var(--red) 0%, var(--red-deep) 100%);
  }
  .front-footer .apply { position: absolute; left: 363px; top: 11px; }
  .apply { color: #fff; font-size: 14px; white-space: nowrap; }

  /* Back */
  .back-header {
    position: absolute; left: 0; top: 0; width: 305px; height: 138px;
    background: linear-gradient(180deg, var(--red) 0%, var(--red-deep) 100%);
    color: #fff; font-weight: 600; font-size: 19px; line-height: 1.6;
    text-align: center; padding: 40px 0 0 0;
  }
  .back-footer {
    position: absolute; left: 0; top: 423px; width: 330px; height: 74px;
    background: var(--charcoal);
  }
  .back-footer .apply { position: absolute; left: 30px; top: 26px; }
  .photo-brand { left: 118px; top: 185px; color: var(--charcoal); font-size: 18px; }
  .postcard--back .promo-title { left: 148px; top: 256px; color: var(--red-text); font-size: 24px; line-height: 1.1; text-align: center; white-space: normal; }
  .contact {
    position: absolute; left: 364px; top: 26px;
    color: var(--charcoal); font-size: 11.5px; line-height: 1.35; font-weight: 600;
  }
  .contact .phone { display: flex; align-items: center; gap: 8px; margin-top: 6px; color: var(--ink-soft); font-weight: 700; }
  .stamp-box {
    position: absolute; left: 548px; top: 22px; width: 77px; height: 54px;
    border: 1.5px solid var(--rule);
  }
  .address-lines { position: absolute; left: 390px; top: 178px; width: 235px; }
  .address-lines span { display: block; height: 27px; border-top: 1.5px solid var(--rule); }
</style>
</head>
<body>

<section class="postcard postcard--front">
  <div class="intro">Non-variable rate credit card.<br>There is no intro APR, always a great rate.</div>
  <ul class="benefits">
    <li><svg width="9" height="8" viewBox="0 0 9 8"><path d="M1 4 L3.5 6.5 L8 1" fill="none" stroke="#4a4a4a" stroke-width="1.6"/></svg>$0 Balance Transfer Fee, always</li>
    <li><svg width="9" height="8" viewBox="0 0 9 8"><path d="M1 4 L3.5 6.5 L8 1" fill="none" stroke="#4a4a4a" stroke-width="1.6"/></svg>Always a fixed low rate,<br>as low as 7.9% APR*</li>
    <li><svg width="9" height="8" viewBox="0 0 9 8"><path d="M1 4 L3.5 6.5 L8 1" fill="none" stroke="#4a4a4a" stroke-width="1.6"/></svg>No penalty APR*</li>
    <li><svg width="9" height="8" viewBox="0 0 9 8"><path d="M1 4 L3.5 6.5 L8 1" fill="none" stroke="#4a4a4a" stroke-width="1.6"/></svg>$0 Annual Fee</li>
  </ul>
  <p class="savings">Not only could you cut your interest rate in half, but you will also save hundreds of dollars by not paying any balance transfer fees - ever.</p>
  <p class="disclaimer">*Annual Percentage Rate. 7.9% is the preferred rate based on qualifying credit.</p>
  <div class="front-footer"><span class="apply">Apply Today! www.brivantalend.org</span></div>

  <svg class="shapes" width="642" height="496" viewBox="0 0 642 496">
    <defs>
      <linearGradient id="photoTone" x1="0" y1="0" x2="0" y2="1">
        <stop offset="0" stop-color="#e6e8e6"/>
        <stop offset="0.55" stop-color="#cdd1cf"/>
        <stop offset="1" stop-color="#b9b3ad"/>
      </linearGradient>
      <clipPath id="frontPhotoClip"><circle cx="20" cy="300" r="305"/></clipPath>
    </defs>
    <circle cx="20" cy="300" r="320" fill="none" stroke="#d8192e" stroke-width="18"/>
    <circle cx="20" cy="300" r="308" fill="#ffffff"/>
    <rect x="0" y="100" width="400" height="396" fill="url(#photoTone)" clip-path="url(#frontPhotoClip)" role="img" aria-label="Photo of a pink cupcake with white frosting and a paper heart topper on a rustic table"/>
  </svg>

  <div class="front-header">
    <span class="brand-name">Brivanta Community<br>Credit Union</span>
    <span class="promo-title">Springtime saver special!</span>
  </div>
</section>

<section class="postcard postcard--back">
  <svg class="shapes" width="642" height="497" viewBox="0 0 642 497">
    <defs>
      <linearGradient id="photoToneBack" x1="0" y1="0" x2="0" y2="1">
        <stop offset="0" stop-color="#e8eae8"/>
        <stop offset="0.6" stop-color="#cfd3d1"/>
        <stop offset="1" stop-color="#bcb6b0"/>
      </linearGradient>
    </defs>
    <rect x="0" y="138" width="330" height="285" fill="url(#photoToneBack)" role="img" aria-label="Photo of a pink cupcake with white frosting and a paper heart topper"/>
  </svg>
  <div class="back-header">When you need OPTIONS,<br>we're here for you</div>
  <div class="back-footer"><span class="apply">Apply Today! www.brivantalend.org</span></div>
  <span class="brand-name photo-brand">Brivanta Community<br>Credit Union</span>
  <span class="promo-title">Springtime<br>saver special!</span>

  <svg class="shapes" width="642" height="497" viewBox="0 0 642 497">
    <path d="M300 0 H642 V497 H292 Q352 250 300 0Z" fill="#ffffff"/>
    <path d="M300 0 H316 Q370 250 306 497 H292 Q352 250 300 0Z" fill="#d8192e"/>
  </svg>

  <div class="contact">
    Address<br>2280 W Alder Ct. Unit 9,<br>Lakewood CO 80228
    <div class="phone">
      <svg width="13" height="13" viewBox="0 0 13 13"><rect width="13" height="13" rx="2" fill="#6d6e71"/><path d="M4 3 L5.5 3 L6 5 L5 5.8 Q6 7.8 7.2 8 L8 7 L10 7.5 L10 9 Q6 10 3.5 5 Z" fill="#fff"/></svg>
      303-555-0142
    </div>
  </div>
  <div class="stamp-box"></div>
  <div class="address-lines"><span></span><span></span><span></span><span></span><span></span></div>
</section>

</body>
</html>
```